vireo nuts company small package

we are looking to design a package for our nuts 10cm by 13 cm and also 3.25 inch by 4.5 inches. our nuts are:
Salted peanuts
honey roasted peanuts
salted cashews
honey roasted cashews
pistachios
sunflower seeds

have a floral design simple yet elegant not too crowded
our product is non GMO

some of our competitors:
http://kestrabite.example/
http://www.dovuhusk.example/sg/
http://tirotiro.example/en/content/view/5/17/

Target Market(s)

european market, Middle eastern market

Industry/Entity Type

It Company

Font styles to use
Decorative
Script

Requirements
Must have
• floral design not crowded yet elegant
• high resolution pictures of the nuts
Nice to have
Should not have
• cartoon characters

```html
<!DOCTYPE html>
<html lang="en">
<head>
<meta charset="utf-8">
<title>Vireo Salted Peanuts – Package Front</title>
<link href="https://fonts.googleapis.com/css2?family=Caveat+Brush&family=Cinzel:wght@700&display=swap" rel="stylesheet">
<style>
  :root {
    --backdrop: #ececec;
    --pack-base: #a6b014;
    --pack-light: #c7d11f;
    --ring-olive: #8d9610;
    --core-yellow: #e4ea1e;
    --window-edge: #d9e21a;
    --nut-light: #e9cfa4;
    --nut-dark: #b88a55;
    --title-orange: #f07a12;
    --title-shadow: #b8490a;
    --label-navy: #1f2347;
    --brand-ink: #ffffff;
    --brand-plate: #141414;
  }
  html, body {
    margin: 0;
    width: 1200px;
    height: 1076px;
    overflow: hidden;
    background: var(--backdrop);
  }
  .canvas {
    position: relative;
    width: 1200px;
    height: 1076px;
  }
  .pack-art {
    position: absolute;
    inset: 0;
  }
  .brand {
    position: absolute;
    left: 508px;
    top: 242px;
    width: 160px;
    height: 76px;
    display: flex;
    align-items: center;
    justify-content: center;
    background: var(--brand-plate);
    font-family: "Cinzel", serif;
    font-weight: 700;
    font-size: 40px;
    color: var(--brand-ink);
    letter-spacing: 1px;
  }
  .product-name {
    position: absolute;
    left: 440px;
    top: 472px;
    width: 330px;
    margin: 0;
    text-align: center;
    font-family: "Caveat Brush", cursive;
    font-weight: 400;
    font-size: 104px;
    line-height: 1;
    letter-spacing: 2px;
    color: var(--title-orange);
    text-shadow: 2px 3px 0 var(--title-shadow);
  }
  .flavour {
    position: absolute;
    left: 588px;
    top: 596px;
    margin: 0;
    font-family: "Cinzel", serif;
    font-weight: 700;
    font-size: 24px;
    color: var(--label-navy);
  }
</style>
</head>
<body>
<main class="canvas">
  <svg class="pack-art" width="1200" height="1076" viewBox="0 0 1200 1076" xmlns="http://www.w3.org/2000/svg">
    <defs>
      <clipPath id="pack-body">
        <rect x="340" y="172" width="500" height="734"/>
      </clipPath>
      <linearGradient id="nut-fill" x1="0" y1="0" x2="1" y2="1">
        <stop offset="0" stop-color="var(--nut-light)"/>
        <stop offset="0.5" stop-color="var(--nut-dark)"/>
        <stop offset="1" stop-color="var(--nut-light)"/>
      </linearGradient>
    </defs>

    <g class="pack" clip-path="url(#pack-body)">
      <rect class="pack-base" x="340" y="172" width="500" height="734" fill="var(--pack-base)"/>
      <ellipse class="outer-glow" cx="590" cy="580" rx="330" ry="430" fill="var(--pack-light)"/>
      <ellipse class="olive-ring" cx="600" cy="590" rx="215" ry="330" fill="var(--ring-olive)"/>
      <ellipse class="mid-ring" cx="600" cy="595" rx="150" ry="270" fill="var(--pack-light)"/>
      <ellipse class="core" cx="600" cy="600" rx="95" ry="170" fill="var(--core-yellow)"/>

      <path class="window-top" role="img" aria-label="Photograph of salted roasted peanuts"
        d="M340 382 C420 362 500 392 580 376 C660 358 740 352 840 360 L840 404 C760 400 680 420 600 432 C520 444 430 430 340 444 Z"
        fill="url(#nut-fill)" stroke="var(--window-edge)" stroke-width="4"/>
      <path class="window-bottom" role="img" aria-label="Photograph of salted roasted peanuts"
        d="M340 738 C430 724 520 740 600 724 C680 710 760 712 840 718 L840 772 C760 766 680 784 600 786 C520 790 430 770 340 782 Z"
        fill="url(#nut-fill)" stroke="var(--window-edge)" stroke-width="4"/>
    </g>

    <path class="crimp-top" d="M340 172 L840 172 L840 186 L340 186 Z" fill="var(--pack-light)" opacity="0.6"/>
    <path class="crimp-bottom" d="M340 892 L840 892 L840 906 L340 906 Z" fill="var(--pack-light)" opacity="0.6"/>
  </svg>

  <div class="brand">VIREO</div>
  <h1 class="product-name">PEANUTS</h1>
  <p class="flavour">SALTED</p>
</main>
</body>
</html>
```